We need 3 A2 posters similar look but different enough to be eye catching when changed.

We are a healthcare centre that requires 3 A2 posters - simple, similar but different background colours. These posters will be used within our business to promote services we provide to our clients.

The design should include our logo(attached), a large header and a large section in the middle of the poster to promote the event. We need a blank text box (which WE can insert text to advertise), and 1 image to advertise the event. Please note, we do not need you to choose an image we simply would like you to place a demo to give us an idea of where it should sit.

We want to use the bubble design (attached) as a background and the company colours pink, orange and blue - as on our website. Attached is a copy of our logo and background bubble effect. You can also refer to our website - www.tallowparkwellness.com.au for more inspiration.

Just to reiterate, these posters should be simple, different but have a uniform feel. They should have an empty middle section that can be edited to add text and a space for an eye catching title and matching image.

Our services include Chiropractic, Podiatry, Nutrition, Massage, Yoga, Pilates and Specialised rehabilitation classes.

Reason: Hi designers, I know we are all busy but I really need more designs from the designers I invited to this project and look forward to receiving more designs. Any questions please let me know. Regards, Marnie

Reason: Hi all Increased the budget Regards Marnie

Corporate Sydney City office workers

Healthcare

• logo and company colours
section in the middles that can be edited to add text
Space allocated for image placement
Catchy title/header

```html
<!DOCTYPE html>
<html lang="en">
<head>
<meta charset="utf-8">
<title>Detox through Massage – Tallow Park Wellness</title>
<link rel="stylesheet" href="https://fonts.googleapis.com/css2?family=Tinos:wght@700&family=Arimo:wght@700&family=Source+Sans+3:wght@400;700&display=swap">
<style>
  :root {
    --lavender: #b4b4da;
    --lavender-light: #c4c4e2;
    --purple: #6462ae;
    --orange: #d98a35;
    --pink: #bf2f80;
    --ink: #111111;
    --body-ink: #1e1e1e;
    --white: #ffffff;
    --photo-light: #eef2f4;
    --photo-mid: #c9d6dc;
    --photo-dark: #8ea3ad;
  }
  * { margin: 0; padding: 0; box-sizing: border-box; }
  html, body { width: 849px; height: 1200px; overflow: hidden; background: var(--white); }
  .poster { position: relative; width: 849px; height: 1200px; overflow: hidden; background: var(--white); }

  .header-field {
    position: absolute; left: 0; top: 0; width: 849px; height: 340px;
    background: linear-gradient(135deg, var(--lavender-light) 0%, var(--lavender) 60%, #aeaed6 100%);
  }
  .poster-title { font-size: 0; }
  .title { position: absolute; line-height: 1; color: var(--ink); white-space: nowrap; }
  .title-detox { left: 33px; top: 25px; font: 700 128px/1 "Tinos", "Times New Roman", serif; letter-spacing: -3px; }
  .title-through { left: 367px; top: 71px; font: 700 72px/1 "Arimo", Arial, sans-serif; letter-spacing: 4px; }
  .title-massage { left: 304px; top: 143px; font: 700 140px/1 "Tinos", "Times New Roman", serif; letter-spacing: 0; }

  .rule { position: absolute; }
  .rule-purple { background: var(--purple); }
  .rule-orange { background: var(--orange); }
  .rule-pink { background: var(--pink); }

  .feature-image {
    position: absolute; left: 0; top: 340px; width: 849px; height: 828px;
    background:
      radial-gradient(ellipse 420px 260px at 30% 25%, var(--photo-light) 0%, transparent 70%),
      radial-gradient(ellipse 380px 300px at 75% 35%, #f3f6f7 0%, transparent 70%),
      radial-gradient(ellipse 500px 240px at 60% 95%, var(--photo-dark) 0%, transparent 75%),
      linear-gradient(160deg, var(--photo-mid) 0%, #dfe7eb 45%, #b3c4cc 100%);
  }

  .promo-copy {
    position: absolute; left: 285px; top: 567px; width: 298px;
    font: 400 16.2px/21.9px "Source Sans 3", "Myriad Pro", Arial, sans-serif;
    color: var(--body-ink);
    hyphens: manual;
  }

  .brand-band {
    position: absolute; left: 284px; top: 910px; width: 565px; height: 63px;
    background: var(--purple);
    display: flex; align-items: center; padding-left: 18px; padding-top: 10px;
  }
  .brand-name {
    font: 700 30px/1 "Source Sans 3", Arial, sans-serif;
    color: var(--white); letter-spacing: -0.5px;
  }
</style>
</head>
<body>
<main class="poster">
  <section class="header-field" role="img" aria-label="Soft lavender background of overlapping rounded bubble squares"></section>

  <h1 class="poster-title">
    <span class="title title-detox">Detox</span>
    <span class="title title-through">through</span>
    <span class="title title-massage">Massage</span>
  </h1>

  <div class="rule rule-purple" style="left:284px; top:307px; width:565px; height:19px;"></div>
  <div class="rule rule-orange" style="left:284px; top:327px; width:565px; height:3px;"></div>
  <div class="rule rule-pink" style="left:284px; top:331px; width:565px; height:8px;"></div>

  <div class="feature-image" role="img" aria-label="Blue-toned photograph of a therapist's hands giving a back massage"></div>

  <p class="promo-copy">The aromatherapy blend and cupping work to quieten the sympathetic nervous system responsible for our stress response commonly known as the “fight or flight response”. Simultaneously they also work to stimulate the parasympa&shy;thetic nervous system which is in charge of our “rest and digest” response. This promotes a calm, healing environment, improves organ function and improves absorption of nutrients making it an ideal integration to a detox program.</p>

  <div class="brand-band">
    <span class="brand-name">Tallow Park Wellness</span>
  </div>

  <div class="rule rule-purple" style="left:0; top:1168px; width:849px; height:14px;"></div>
  <div class="rule rule-orange" style="left:0; top:1184px; width:849px; height:3px;"></div>
  <div class="rule rule-pink" style="left:0; top:1189px; width:849px; height:6px;"></div>
</main>
</body>
</html>
```